Quillpost Banner

Hi, I need help making banners for my social media channels. Once we make one banner all the other banners will follow the same look and feel. Please help me design my Quillpost page banner to start.

Attached is my branding guidelines - please choose a design that fits within my Branding Guidelines. Please note that I only use two fonts. Belanosima and Arial. I have also attached screenshots of my Gravlo channel and Zapnix thumbnails. I made banners already but I am not happy with them. Please take into account my whole “brand universe” to create the banner.

The message I want to convey in the banner is that I offer tours of factories in Vietnam. I offer to take clients on factory tours and the tours include car, driver and translator.

If you have any questions then please don't hesitate to ask.

I have included images of factory tours. I also included my logo in case you want to use it.

```html
<!DOCTYPE html>
<html lang="en">
<head>
<meta charset="utf-8">
<title>Quillpost Banner – Factory Tours</title>
<link rel="stylesheet" href="https://fonts.googleapis.com/css2?family=Belanosima:wght@400;600;700&display=swap">
<style>
  :root {
    --bg-deep: #240833;
    --bg-mid: #33104a;
    --logo-box: #2c0d3f;
    --ink-light: #ffffff;
    --ink-soft: #e6dfe6;
    --ink-dark: #2a0a36;
    --salmon: #f99b7d;
    --teal: #6cbdbd;
    --dot: #c27bd0;
    --ring-top: #8e2a74;
    --ring-left: #d86a6a;
    --ring-right: #f08a6e;
    --ring-bottom: #b474c4;
    --ring-center: #3a0f4a;
  }
  * { margin: 0; padding: 0; box-sizing: border-box; }
  html, body { width: 1200px; height: 457px; overflow: hidden; background: var(--bg-deep); }
  .banner {
    position: relative;
    width: 1200px; height: 457px; overflow: hidden;
    background:
      radial-gradient(ellipse 420px 180px at 200px 420px, rgba(90,40,110,.35), transparent 70%),
      radial-gradient(ellipse 500px 260px at 520px 120px, rgba(70,25,90,.35), transparent 70%),
      linear-gradient(180deg, var(--bg-mid), var(--bg-deep));
    font-family: Arial, Helvetica, sans-serif;
  }
  .brand-mark {
    position: absolute; left: 29px; top: 22px; width: 152px; height: 70px;
    background: var(--logo-box);
    display: flex; align-items: center; justify-content: center; flex-direction: column;
    color: var(--ink-light); font-family: Arial, Helvetica, sans-serif;
    font-weight: 700; font-size: 16px; line-height: 1.1; text-align: center;
  }
  .dots { position: absolute; }
  .headline-visit {
    position: absolute; left: 220px; width: 200px; top: 100px; text-align: center;
    color: var(--ink-soft); font-size: 33px; letter-spacing: .5px;
  }
  .pill {
    position: absolute; background: var(--salmon); color: var(--ink-dark);
    border-radius: 14px; display: flex; align-items: center; justify-content: center;
  }
  .pill-factories { left: 181px; top: 146px; width: 278px; height: 46px; font-weight: 700; font-size: 33px; }
  .pill-includes { left: 106px; top: 320px; width: 448px; height: 46px; font-size: 34px; border-radius: 8px; }
  .headline-country { position: absolute; left: 0; top: 0; }
  .tour-wheel { position: absolute; left: 0; top: 0; }
</style>
</head>
<body>
<div class="banner">
  <div class="brand-mark"><span>Delta Mill</span><span>Tours</span></div>

  <svg class="dots" width="1200" height="457" viewBox="0 0 1200 457" aria-hidden="true">
    <g fill="var(--dot)">
      <rect x="516" y="60" width="138" height="4" fill="url(#dotRow)"/>
      <rect x="540" y="67" width="140" height="4" fill="url(#dotRow)"/>
      <rect x="44" y="401" width="140" height="4" fill="url(#dotRow)"/>
      <rect x="70" y="409" width="139" height="4" fill="url(#dotRow)"/>
    </g>
    <defs>
      <pattern id="dotRow" width="8" height="4" patternUnits="userSpaceOnUse">
        <rect width="5" height="4" fill="var(--dot)"/>
      </pattern>
    </defs>
  </svg>

  <div class="headline-visit">VISIT</div>
  <div class="pill pill-factories">FACTORIES IN</div>

  <svg class="headline-country" width="1200" height="457" viewBox="0 0 1200 457">
    <text x="44" y="300" font-family="Belanosima, sans-serif" font-weight="700" font-size="128"
          fill="var(--teal)" textLength="552" lengthAdjust="spacingAndGlyphs">VIETNAM</text>
  </svg>

  <div class="pill pill-includes">Car + Driver + Translator</div>

  <svg class="tour-wheel" width="1200" height="457" viewBox="0 0 1200 457">
    <defs>
      <clipPath id="wedgeTop"><polygon points="909,228 609,-72 1209,-72"/></clipPath>
      <clipPath id="wedgeRight"><polygon points="909,228 1209,-72 1209,528"/></clipPath>
      <clipPath id="wedgeBottom"><polygon points="909,228 1209,528 609,528"/></clipPath>
      <clipPath id="wedgeLeft"><polygon points="909,228 609,528 609,-72"/></clipPath>
      <linearGradient id="photoTop" x1="0" y1="0" x2="0" y2="1">
        <stop offset="0" stop-color="#9fb4c4"/><stop offset="1" stop-color="#6f6a5c"/>
      </linearGradient>
      <linearGradient id="photoLeft" x1="0" y1="0" x2="1" y2="1">
        <stop offset="0" stop-color="#c9bfa8"/><stop offset="1" stop-color="#6f6658"/>
      </linearGradient>
      <linearGradient id="photoRight" x1="0" y1="0" x2="0" y2="1">
        <stop offset="0" stop-color="#3a3a3c"/><stop offset="1" stop-color="#8c7f73"/>
      </linearGradient>
      <linearGradient id="photoBottom" x1="0" y1="0" x2="0" y2="1">
        <stop offset="0" stop-color="#c8cfd6"/><stop offset="1" stop-color="#8a6a52"/>
      </linearGradient>
      <linearGradient id="photoCenter" x1="0" y1="0" x2="0" y2="1">
        <stop offset="0" stop-color="#dcd6d4"/><stop offset="1" stop-color="#3b4a66"/>
      </linearGradient>
    </defs>

    <g clip-path="url(#wedgeTop)">
      <circle cx="909" cy="228" r="227" fill="var(--ring-top)"/>
      <circle cx="909" cy="228" r="219" fill="url(#photoTop)" role="img" aria-label="Photo: visitors walking past shoe racks in a footwear factory"/>
      <circle cx="909" cy="228" r="96" fill="var(--ring-top)"/>
    </g>
    <g clip-path="url(#wedgeLeft)">
      <circle cx="909" cy="228" r="227" fill="var(--ring-left)"/>
      <circle cx="909" cy="228" r="219" fill="url(#photoLeft)" role="img" aria-label="Photo: workers in a furniture workshop"/>
      <circle cx="909" cy="228" r="96" fill="var(--ring-left)"/>
    </g>
    <g clip-path="url(#wedgeRight)">
      <circle cx="909" cy="228" r="227" fill="var(--ring-right)"/>
      <circle cx="909" cy="228" r="219" fill="url(#photoRight)" role="img" aria-label="Photo: tour group inspecting goods in a factory hall"/>
      <circle cx="909" cy="228" r="96" fill="var(--ring-right)"/>
    </g>
    <g clip-path="url(#wedgeBottom)">
      <circle cx="909" cy="228" r="227" fill="var(--ring-bottom)"/>
      <circle cx="909" cy="228" r="219" fill="url(#photoBottom)" role="img" aria-label="Photo: visitors reviewing leather shoe samples on racks"/>
      <circle cx="909" cy="228" r="96" fill="var(--ring-bottom)"/>
    </g>

    <g stroke="var(--bg-deep)" stroke-width="12">
      <line x1="669" y1="-12" x2="1149" y2="468"/>
      <line x1="1149" y1="-12" x2="669" y2="468"/>
    </g>
    <circle cx="909" cy="228" r="88" fill="var(--ring-center)"/>
    <circle cx="909" cy="228" r="74" fill="url(#photoCenter)" role="img" aria-label="Portrait photo of the tour host"/>

    <path d="M889 457 Q 960 250 1200 208" fill="none" stroke="var(--ink-light)" stroke-width="1.5"/>
  </svg>
</div>
</body>
</html>
```